Website Design for a holiday home letting busines

We require a redesign of our present website www.birchwoodstays.com. We want the website to stand out and look professional and clean to make holiday hunters want to book a caravan or lodge holiday with us. Our logo is red however we DO NOT want the website to be red. We want a natural colour scheme.

The final design should communicate that we are a professional company to book with.

On the home page we require;
Overview of company
Photo
Search box for holiday (check in)
Late Deals
Reviews
News

We would like the following pages designed; home page, available dates page, caravans page, content page.

The website should be responsive for smart phones. One website I do like is http://www.verdamoro.be/nl/

Target Market(s)

Families

Industry/Entity Type

Travel

Number of Pages Required

5+ page

Font styles to use
Serif

Requirements
Must have
• The project must be responsive for mobile phones and tablets.
• Ability to search for holiday home holidays
• We want a natural colour scheme.
Nice to have
• A style we like is http://www.verdamoro.be/nl/
Should not have
• Do not use red as a colour for the website. Our logo is red so this is the only time we want this used.

```html
<!DOCTYPE html>
<html lang="en">
<head>
<meta charset="utf-8">
<title>Birchwood Stays – Private Holiday Rentals</title>
<link href="https://fonts.googleapis.com/css2?family=Open+Sans:wght@400;600;700;800&family=Roboto+Slab:wght@400;700&display=swap" rel="stylesheet">
<style>
:root{
  --olive:#8f8d4f;
  --olive-dark:#6f6d38;
  --tan:#c8b98b;
  --tan-light:#d8cca4;
  --sage:#8fae6c;
  --sage-band:#a3bd83;
  --green-dark:#5f7d43;
  --red:#d9382c;
  --ink:#333;
  --muted:#777;
  --white:#fff;
  --foot:#efefec;
  --foot-dark:#4d4d48;
}
*{box-sizing:border-box;margin:0;padding:0}
html,body{width:1200px;height:2472px;overflow:hidden}
body{font-family:"Open Sans",Arial,sans-serif;color:var(--ink);background:var(--white);position:relative}
.abs{position:absolute}
/* hero */
.hero{position:absolute;left:0;top:0;width:1200px;height:600px;background:linear-gradient(180deg,#b7c7d6 0%,#d9cdb4 45%,#b99e7a 100%)}
.brand{position:absolute;left:470px;top:18px;width:260px;height:76px;background:var(--white);border-radius:0 0 8px 8px;display:flex;align-items:center;justify-content:center;gap:10px;box-shadow:0 2px 6px rgba(0,0,0,.15)}
.brand-dot{width:34px;height:34px;border-radius:50%;background:var(--red)}
.brand-name{font-family:"Roboto Slab",Georgia,serif;font-weight:700;font-size:24px;color:var(--red)}
.brand-sub{position:absolute;left:470px;top:98px;width:260px;text-align:center;font-size:12px;color:var(--ink)}
.nav{position:absolute;left:70px;top:150px;width:1060px;height:42px;background:var(--olive);display:flex;align-items:center;padding-left:30px;gap:26px}
.nav a{color:var(--white);font-size:13px;font-weight:600;text-decoration:none}
.hero-title{position:absolute;left:140px;top:292px;font-size:40px;font-weight:800;color:var(--white);letter-spacing:1px}
.hero-sub{position:absolute;left:140px;top:346px;width:330px;font-size:17px;line-height:24px;color:var(--white)}
.btn-more{position:absolute;left:140px;top:424px;padding:10px 20px;background:var(--olive);color:var(--white);font-size:15px;font-weight:600;border-radius:3px}
.photo-circle{position:absolute;border-radius:50%;border:6px solid var(--white);background:linear-gradient(160deg,#8fb7d8,#e0c48d 55%,#6e9a55)}
/* booking + about */
.tan-band{position:absolute;left:0;top:600px;width:1200px;height:560px;background:var(--tan)}
.booking{position:absolute;left:120px;top:640px;width:960px;height:94px;background:#efe9d7;display:flex;align-items:center;box-shadow:0 2px 4px rgba(0,0,0,.15)}
.booking-label{width:220px;height:100%;background:var(--olive);color:var(--white);padding:18px 22px}
.booking-label h3{font-size:24px;font-weight:600}
.booking-label p{font-size:11px}
.field{margin-left:22px;width:156px}
.field label{display:block;font-size:11px;color:var(--muted);margin-bottom:4px}
.field div{height:30px;background:var(--white);border:1px solid #ccc;font-size:11px;padding:7px 8px;color:#666}
.btn-book{margin-left:28px;background:var(--red);color:var(--white);font-size:17px;font-weight:600;padding:12px 20px;border-radius:3px}
.video{position:absolute;left:120px;top:800px;width:380px;height:280px;background:linear-gradient(160deg,#3b4f6a,#5b7a8c 60%,#6d8a5e)}
.play{position:absolute;left:162px;top:112px;width:56px;height:56px;border-radius:50%;background:rgba(255,255,255,.85)}
.about{position:absolute;left:540px;top:800px;width:540px}
.about h2{font-size:26px;font-weight:700;color:var(--ink);margin-bottom:14px}
.about p{font-size:13px;line-height:20px;color:#4a4530;margin-bottom:12px}
/* cards */
.sec-title{position:absolute;left:0;width:1200px;text-align:center;font-size:34px;font-weight:600;color:var(--green-dark)}
.rule{position:absolute;left:560px;width:80px;height:3px;background:var(--olive)}
.cards{position:absolute;left:120px;width:960px;height:190px;display:flex;gap:13px}
.card{flex:1;height:190px}
.card-info{background:var(--sage);color:var(--white);text-align:center;padding-top:16px}
.card-info h4{font-size:18px;font-weight:600;padding-bottom:10px;border-bottom:1px solid rgba(255,255,255,.5);margin:0 16px 10px}
.card-info p{font-size:12px;line-height:19px}
.card-photo{background:linear-gradient(150deg,#d8dde0,#f4f2ec 50%,#8da7b8)}
/* reviews */
.green-band{position:absolute;left:0;top:1860px;width:1200px;height:440px;background:var(--sage-band)}
.band-title{position:absolute;left:120px;top:1900px;width:700px;text-align:center;font-size:30px;font-weight:600;color:var(--white)}
.avatar{position:absolute;left:420px;top:1960px;width:96px;height:96px;border-radius:50%;border:4px solid var(--white);background:linear-gradient(#c9c2b0,#7d8a95)}
.quote{position:absolute;left:160px;top:2090px;width:620px;font-size:13px;line-height:20px;color:var(--white);text-align:center}
.reviewer{position:absolute;left:120px;top:2160px;width:700px;text-align:center;color:var(--white);font-size:13px}
.stars{position:absolute;left:440px;top:2210px}
.news{position:absolute;left:888px;top:1966px;width:282px;height:326px;background:var(--white);padding:10px 14px}
.news h4{font-size:13px;font-weight:700;color:var(--green-dark);border-bottom:2px solid var(--sage);padding-bottom:6px;margin-bottom:8px}
.news-item{border-bottom:1px solid #e2e2e2;padding:8px 0}
.news-item p{font-size:11px;line-height:15px;color:#555}
.news-item span{font-size:10px;color:var(--olive)}
/* footer */
.footer{position:absolute;left:0;top:2300px;width:1200px;height:132px;background:var(--foot)}
.fcol{position:absolute;top:2316px}
.fcol h5{font-size:14px;font-weight:700;color:var(--green-dark);margin-bottom:6px}
.fcol li{list-style:none;font-size:11px;line-height:15px;color:#555}
.badge{position:absolute;left:1010px;top:2316px;width:96px;height:96px;border-radius:50%;background:var(--sage)}
.bottom{position:absolute;left:0;top:2432px;width:1200px;height:40px;background:var(--foot-dark);color:#cfcfc8;font-size:10px;padding:8px 120px 0 40px;line-height:12px}
.social{position:absolute;top:2440px;width:24px;height:24px;border-radius:50%;background:var(--sage)}
</style>
</head>
<body>

<section class="hero" role="img" aria-label="Photo of hot air balloons drifting over rocky valley landscape"></section>
<div class="brand"><span class="brand-dot"></span><span class="brand-name">Birchwood Stays</span></div>
<div class="brand-sub">at Thornbury Vale Holiday Park</div>
<nav class="nav">
  <a>Home</a><a>News</a><a>Reviews</a><a>Caravans &amp; Lodges</a><a>2015 Holidays</a><a>2016 Holidays</a><a>Payment Plans</a><a>Thornbury Vale</a><a>Local Attractions</a><a>Contact</a>
</nav>
<h1 class="hero-title">PRIVATE HOLIDAY RENTALS</h1>
<p class="hero-sub">Quality Lodge &amp; Caravans to hire at Thornbury Vale Holiday Park, Northumberland</p>
<div class="btn-more">Know More</div>
<div class="photo-circle" style="left:800px;top:220px;width:220px;height:220px" role="img" aria-label="Photo of a holiday villa with pool"></div>
<div class="photo-circle" style="left:730px;top:330px;width:110px;height:110px" role="img" aria-label="Photo of a lodge exterior"></div>
<div class="photo-circle" style="left:1010px;top:250px;width:80px;height:80px" role="img" aria-label="Photo of a garden terrace"></div>
<div class="photo-circle" style="left:990px;top:360px;width:90px;height:90px" role="img" aria-label="Photo of a swimming pool"></div>

<div class="tan-band"></div>
<form class="booking">
  <div class="booking-label"><h3>Online Booking</h3><p>Find your perfect break in seconds</p></div>
  <div class="field"><label>Type of stay</label><div>Select a type of stay ▾</div></div>
  <div class="field"><label>Check in date</label><div>DD/MM/YYYY</div></div>
  <div class="field"><label>Check out date</label><div>DD/MM/YYYY</div></div>
  <div class="field" style="width:100px"><label>Guests</label><div>2 ▾</div></div>
  <div class="btn-book">Book now</div>
</form>
<div class="video" role="img" aria-label="Video still of a caravan holiday park">
  <svg class="play" viewBox="0 0 56 56"><circle cx="28" cy="28" r="28" fill="#fff" opacity=".85"/><path d="M22 17 L40 28 L22 39Z" fill="#6f6d38"/></svg>
</div>
<div class="about">
  <h2>NO DEPOSIT HOLIDAYS</h2>
  <p>We are pleased to offer 2016 breaks at our lodges and caravans at Thornbury Vale Holiday Park with no deposit required.</p>
  <p>We have flexible dates for weekday and weekend breaks, with a wide choice of homes so you can pick the one that suits your family best.</p>
  <p>Once you add to the basket you choose your dates and the number of guests. You can then pay the full amount at any time before arrival.</p>
  <p>If you have any questions please call our team who will be glad to help with planning your stay.</p>
</div>

<h2 class="sec-title" style="top:1190px">OUR CARAVANS &amp; LODGES</h2>
<div class="rule" style="top:1244px"></div>
<div class="cards" style="top:1262px">
  <div class="card card-info"><h4>Larch Hollow</h4><p>Three bedroom lodge<br>Sleeps up to six<br>Hot tub deck<br>Dog friendly</p></div>
  <div class="card card-photo" role="img" aria-label="Photo of a caravan lounge"></div>
  <div class="card card-photo" role="img" aria-label="Photo of a lodge interior"></div>
  <div class="card card-photo" role="img" aria-label="Photo of a caravan kitchen"></div>
</div>

<h2 class="sec-title" style="top:1530px">LATE DEALS</h2>
<div class="rule" style="top:1584px"></div>
<div class="cards" style="top:1602px">
  <div class="card card-info"><h4>Larch Hollow</h4><p>Three nights from £199<br>Sleeps up to six<br>Arrive this Friday<br>Book today</p></div>
  <div class="card card-photo" role="img" aria-label="Photo of a caravan bedroom"></div>
  <div class="card card-photo" role="img" aria-label="Photo of a lodge living room"></div>
  <div class="card card-photo" role="img" aria-label="Photo of a dining area"></div>
</div>

<div class="green-band"></div>
<h2 class="band-title">WHAT DO CUSTOMERS SAY?</h2>
<div class="avatar" role="img" aria-label="Portrait photo of a customer"></div>
<p class="quote">“We had a lovely week in the lodge, everything was spotless and the children loved the park. We will certainly be booking again next summer with the whole family.”</p>
<p class="reviewer"><strong>Daniel Ashford</strong><br>Guest, Larch Hollow</p>
<svg class="stars" width="60" height="14" viewBox="0 0 60 14"><g fill="#fff"><path d="M7 0l2 5h5l-4 3 2 5-5-3-5 3 2-5-4-3h5z"/><path d="M29 0l2 5h5l-4 3 2 5-5-3-5 3 2-5-4-3h5z"/><path d="M51 0l2 5h5l-4 3 2 5-5-3-5 3 2-5-4-3h5z"/></g></svg>
<aside class="news">
  <h4>LATEST NEWS</h4>
  <div class="news-item"><p>New lodges arrive on the park for the 2016 season, now open to book.</p><span>Read More</span></div>
  <div class="news-item"><p>Summer entertainment guide for families staying at the park this year.</p><span>Read More</span></div>
  <div class="news-item"><p>Spring short breaks now on sale with no deposit needed.</p><span>Read More</span></div>
  <div class="news-item"><p>Our new payment plans make booking easier than ever.</p><span>Read More</span></div>
</aside>

<footer class="footer"></footer>
<div class="fcol" style="left:120px"><h5>Navigation</h5><ul><li>About Us</li><li>News</li><li>Caravans &amp; Lodges</li><li>2015 Holidays</li><li>2016 Holidays</li><li>Late Deals</li></ul></div>
<div class="fcol" style="left:370px"><h5>More Link</h5><ul><li>Thornbury Vale</li><li>Local Attractions</li><li>Gallery</li><li>Contact Us</li><li>Reviews</li></ul></div>
<div class="fcol" style="left:610px"><h5>More Link</h5><ul><li>Frequently Asked Questions</li><li>Terms and Conditions</li><li>Privacy Policy</li><li>Booking Terms</li></ul></div>
<div class="badge" role="img" aria-label="Review rating badge"></div>
<div class="bottom">© Birchwood Stays. All lodges and caravans are privately owned and let at Thornbury Vale Holiday Park. www.birchwoodstays.com – all rights reserved.</div>
<div class="social" style="left:1100px"></div>
<div class="social" style="left:1130px"></div>
<div class="social" style="left:1160px"></div>
</body>
</html>
```